Long Term Insurance for Maturing Women

My business, is a Full service Life and Property Insurance Agency.. I want a reply card, Gloss, with woman showing Maturity, on a beach looking out at a Sun Set, with light Colors of Rainbow.
Thinking: If I am alone, how much income will I need to pay for a Long Term Sickness or Injury. ?
Do I have enough money set aside to cover the added expenses of a long Term Illness ?
Have I enough Life Insurance to cover final expenses, and leave my love ones free of any Debt from my Passing ?
These are real life's concerns, Please Call, let's start finding answers today !
Mark Dunstover, Agent # 0718294 at (714-555-3087) - Halvern Insurance & Financial Service LLC.
Markdun@halverninsx.com 4170 Tamsen Ave, Cypress Ca. 90512

Industry/Entity Type

Business

```html
<!DOCTYPE html>
<html lang="en">
<head>
<meta charset="utf-8">
<title>Reply Card – Long Term Insurance</title>
<link href="https://fonts.googleapis.com/css2?family=Arimo:wght@400;700&family=Archivo+Black&family=Roboto+Condensed:wght@400;700&display=swap" rel="stylesheet">
<style>
  :root {
    --amber: #b0650f;
    --amber-dark: #97560e;
    --navy: #1f3b8c;
    --ink: #3a2608;
    --alert: #c43a1c;
    --paper: #ffffff;
    --rule: #9aa3b5;
  }
  html, body { margin: 0; padding: 0; overflow: hidden; }
  body { width: 1200px; height: 924px; background: var(--paper); }
  .card { position: relative; width: 1200px; height: 924px; overflow: hidden; font-family: "Arimo", Arial, sans-serif; }

  .scene {
    position: absolute; left: 0; top: 0; width: 1200px; height: 765px;
    background:
      radial-gradient(ellipse 420px 220px at 900px 500px, rgba(255,246,190,0.95), rgba(255,220,120,0) 70%),
      linear-gradient(180deg, #f6f1de 0%, #f4e7b8 35%, #f1c95e 58%, #e8a93a 66%, #d9b36a 78%, #e6cfa2 100%);
  }
  .scene-figure {
    position: absolute; left: 0; top: 95px; width: 640px; height: 670px;
    background: linear-gradient(180deg, rgba(238,230,214,0.75) 0%, rgba(196,226,236,0.7) 45%, rgba(232,222,200,0.75) 100%);
    border-radius: 260px 260px 0 0;
  }

  .headline {
    position: absolute; left: 368px; top: 28px; margin: 0;
    font-weight: 400; font-size: 117px; line-height: 1; letter-spacing: -2px;
    color: var(--amber); white-space: nowrap;
  }
  .subhead {
    position: absolute; left: 373px; top: 150px; margin: 0;
    font-weight: 700; font-size: 27px; line-height: 36px; color: var(--amber-dark);
  }
  .question {
    position: absolute; left: 527px; margin: 0;
    font-size: 24px; line-height: 33px; color: var(--ink);
  }
  .question strong { color: var(--navy); }
  .q-savings { top: 256px; }
  .q-life { top: 346px; }

  .call-out {
    position: absolute; left: 680px; top: 578px; margin: 0;
    font-family: "Archivo Black", "Arial Black", sans-serif;
    font-size: 31px; line-height: 39px; letter-spacing: 0.5px;
    color: var(--alert); -webkit-text-stroke: 1px #f6e6c4;
  }

  .footer { position: absolute; left: 0; top: 765px; width: 1200px; height: 159px; background: var(--paper); }
  .agent { position: absolute; left: 67px; top: 42px; text-align: center; font-family: "Roboto Condensed", Arial, sans-serif; color: var(--navy); }
  .agent-name { margin: 0; font-weight: 700; font-size: 38px; line-height: 42px; }
  .agent-id { margin: 0; font-size: 25px; line-height: 30px; }

  .contact { position: absolute; left: 416px; top: 26px; color: var(--navy); }
  .phone { display: flex; align-items: center; gap: 10px; font-family: "Arimo", Arial, sans-serif; font-weight: 700; font-size: 50px; line-height: 60px; margin: 0; }
  .email { display: flex; align-items: center; gap: 12px; margin: 6px 0 0 38px; font-family: "Roboto Condensed", Arial, sans-serif; font-size: 28px; }

  .divider { position: absolute; left: 886px; top: 16px; width: 1px; height: 124px; background: var(--rule); }
  .agency { position: absolute; left: 918px; top: 20px; font-family: "Roboto Condensed", Arial, sans-serif; color: var(--navy); font-size: 21px; line-height: 29px; }
  .agency-name { margin: 0; font-weight: 700; }
  .agency-address { margin: 0; font-style: normal; }
</style>
</head>
<body>
<div class="card">
  <div class="scene" role="img" aria-label="Photo of a smiling mature woman seated on a beach at golden sunset, sea and sun behind her">
    <div class="scene-figure"></div>
  </div>

  <h1 class="headline">IF I AM ALONE,</h1>
  <p class="subhead">HOW MUCH INCOME WILL I NEED TO PAY<br>FOR A LONG TERM SICKNESS OR INJURY ?</p>

  <p class="question q-savings"><strong>Do I have enough money</strong> set aside to cover<br>the added expenses of a long Term Illness ?</p>
  <p class="question q-life"><strong>Have I enough Life Insurance</strong> to cover<br>final expenses, and leave my love ones<br>free of any Debt from my Passing ?</p>

  <p class="call-out">THESE ARE REAL LIFE’S<br>CONCERNS, PLEASE CALL,<br>LET’S START FINDING<br>ANSWERS TODAY !</p>

  <footer class="footer">
    <div class="agent">
      <p class="agent-name">MARK DUNSTOVER</p>
      <p class="agent-id">Agent # 0718294</p>
    </div>

    <div class="contact">
      <p class="phone">
        <svg width="44" height="44" viewBox="0 0 44 44" aria-hidden="true">
          <circle cx="22" cy="22" r="19" fill="none" stroke="#1f3b8c" stroke-width="3"/>
          <path d="M15 11c2-1 3 0 4 2l1 4c0 1-1 2-2 3 1 3 3 5 6 6 1-1 2-2 3-2l4 1c2 1 3 2 2 4-1 2-3 3-5 3-8-1-14-7-15-15 0-2 1-5 2-6z" fill="#1f3b8c"/>
        </svg>
        (714-555-3087)
      </p>
      <p class="email">
        <svg width="30" height="20" viewBox="0 0 30 20" aria-hidden="true">
          <rect x="0" y="0" width="30" height="20" fill="#1f3b8c"/>
          <path d="M1 1l14 11L29 1" fill="none" stroke="#ffffff" stroke-width="2"/>
          <path d="M1 19l10-9M29 19l-10-9" fill="none" stroke="#ffffff" stroke-width="1.5"/>
        </svg>
        Markdun@halverninsx.com
      </p>
    </div>

    <div class="divider"></div>

    <div class="agency">
      <p class="agency-name">Halvern Insurance<br>&amp; Financial Service LLC.</p>
      <address class="agency-address">4170 Tamsen Ave,<br>Cypress Ca. 90512</address>
    </div>
  </footer>
</div>
</body>
</html>
```